Bref créative
The Quiet Fiddler
Notes on the Path Melodic
Rex Pembury
This is a revised e-book edition of a didactic memoir that has earned praise from major recording artists, symphonic musicians, and music-industry leaders. The book contains musical and social commentary; advice; interviews; memories of America, Europe, and the Middle East; and reference material.
Music
Drummers and other musicians, students, parents, baby boomers, and anyone else who enjoys musical stories, tips, and information.
The author is primarily a drum-set player and timpanist. Any image of a drum set should feature Stanmore drums and Vorkel cymbals (preferably from the 1960s); no other brands are acceptable. (Visit these companies' Web sites and oldstanmorekits.example for ideas.) Photos of 18th-century timpani (kettledrums) are equally appropriate. A photomontage will work, provided it is uncluttered and will reproduce well online (Tindral, eTomes, Cobb & Fairley, et al.).

```html
<!DOCTYPE html>
<html lang="en">
<head>
<meta charset="utf-8">
<title>The Quiet Fiddler — Cover</title>
<link rel="stylesheet" href="https://fonts.googleapis.com/css2?family=Cormorant+Garamond:ital,wght@1,400;1,500&display=swap">
<style>
  :root {
    --frame-black: #000000;
    --page-white: #ffffff;
    --cover-brown: #2d1b11;
    --cover-text: #f3ece2;
    --sepia-pale: #efe6d8;
    --sepia-light: #d9c8b0;
    --sepia-mid: #a88c6c;
    --sepia-deep: #6a5240;
    --sepia-dark: #3c2b1f;
  }
  * { margin: 0; padding: 0; box-sizing: border-box; }
  html, body {
    width: 1200px;
    height: 847px;
    overflow: hidden;
    background: var(--page-white);
  }
  .sheet {
    position: relative;
    width: 1200px;
    height: 847px;
    background: var(--page-white);
    border: 7px solid var(--frame-black);
  }
  .cover {
    position: absolute;
    left: 41px;
    top: 36px;
    width: 559px;
    height: 763px;
    background: var(--cover-brown);
    font-family: "Cormorant Garamond", "EB Garamond", Georgia, serif;
    color: var(--cover-text);
  }
  .cover__author {
    position: absolute;
    top: 0;
    left: 0;
    width: 100%;
    height: 70px;
    display: flex;
    align-items: center;
    justify-content: center;
    font-style: italic;
    font-size: 17px;
    letter-spacing: 0.04em;
  }
  .cover__artwork {
    position: absolute;
    left: 4px;
    top: 78px;
    width: 551px;
    height: 470px;
    border-top: 4px solid var(--page-white);
    background:
      radial-gradient(ellipse 95px 110px at 22% 62%, var(--sepia-pale) 0%, rgba(239,230,216,0.85) 55%, rgba(239,230,216,0) 100%),
      radial-gradient(ellipse 70px 40px at 40% 28%, rgba(60,43,31,0.55) 0%, rgba(60,43,31,0) 100%),
      radial-gradient(ellipse 160px 70px at 60% 82%, rgba(60,43,31,0.7) 0%, rgba(60,43,31,0) 100%),
      radial-gradient(ellipse 120px 60px at 10% 88%, rgba(239,230,216,0.9) 0%, rgba(239,230,216,0) 100%),
      radial-gradient(ellipse 200px 120px at 75% 15%, rgba(239,230,216,0.8) 0%, rgba(239,230,216,0) 100%),
      linear-gradient(180deg, var(--sepia-light) 0%, var(--sepia-mid) 45%, var(--sepia-deep) 75%, var(--sepia-dark) 100%);
  }
  .cover__artwork-rule {
    position: absolute;
    left: 0;
    top: 548px;
    width: 100%;
    height: 5px;
    background: var(--page-white);
  }
  .cover__titles {
    position: absolute;
    left: 0;
    top: 553px;
    width: 100%;
    height: 210px;
    text-align: center;
  }
  .cover__title {
    margin-top: 46px;
    font-style: italic;
    font-weight: 400;
    font-size: 58px;
    line-height: 1;
    letter-spacing: 0.02em;
  }
  .cover__subtitle {
    margin-top: 18px;
    font-style: italic;
    font-weight: 400;
    font-size: 20px;
    letter-spacing: 0.3em;
  }
</style>
</head>
<body>
  <main class="sheet">
    <section class="cover">
      <p class="cover__author">Rex Pembury</p>
      <div class="cover__artwork" role="img" aria-label="Sepia photomontage of a vintage 1960s drum kit with cymbals on a wooden floor, sheet music behind it and a small drummer figure at the left"></div>
      <div class="cover__artwork-rule"></div>
      <div class="cover__titles">
        <h1 class="cover__title">The Quiet Fiddler</h1>
        <p class="cover__subtitle">Notes on the Path Melodic</p>
      </div>
    </section>
  </main>
</body>
</html>
```